Stationary for a Manufacturing Company focused on R&D
Twin-Kay please refer to the concluded Logo Project
Stationary for a Manufacturing Company focused on R&D - Manufacturing
Creative Brief
Use same font as used in my logo
Yes please refer to the log - keep the background colors simple
Modern
Vikram Talwarkar
Stationary for a Manufacturing company
Rustomji Parekh Building, 58 Hill Street, Fortm Mumbai 400019 India
vikram@twin-kay.com
www.twin-kay.com
The card must show advancement - something different but easy to duplicate.....
no information on the back - maybe just the logo at the back could be ok

```html
<!DOCTYPE html>
<html lang="en">
<head>
<meta charset="utf-8">
<title>Twin-Kay Business Card</title>
<link rel="stylesheet" href="https://fonts.googleapis.com/css2?family=Exo+2:wght@400;600;700&display=swap">
<style>
  :root {
    --page-bg: #e9ebe8;
    --card-white: #ffffff;
    --green-deep: #3f6b35;
    --green-mid: #5a8a4c;
    --green-light: #8fb57f;
    --green-pale: #cfe0c6;
    --ink: #4b4f4a;
    --ink-soft: #7a7f78;
  }
  * { margin: 0; padding: 0; box-sizing: border-box; }
  html, body { width: 1200px; height: 1002px; overflow: hidden; }
  body {
    background: var(--page-bg);
    font-family: "Exo 2", sans-serif;
    position: relative;
  }
  .card {
    position: absolute;
    width: 520px;
    height: 298px;
    border-radius: 22px;
    overflow: hidden;
    box-shadow: 0 6px 18px rgba(0,0,0,0.14);
  }
  .card-front { left: 60px; top: 352px; background: var(--card-white); }
  .card-back {
    left: 620px; top: 352px;
    background: radial-gradient(ellipse at 70% 60%, var(--green-mid) 0%, var(--green-deep) 80%);
  }

  .brand {
    position: absolute; left: 34px; top: 34px;
    display: flex; align-items: center; gap: 12px;
  }
  .brand-mark {
    width: 34px; height: 34px; border-radius: 50%;
    background: var(--green-mid);
  }
  .brand-name {
    font-size: 34px; font-weight: 700; letter-spacing: 4px;
    color: var(--green-deep); text-transform: uppercase;
  }
  .brand-tagline {
    position: absolute; left: 230px; top: 78px;
    font-size: 8px; letter-spacing: 1.5px; color: var(--ink-soft);
    text-transform: uppercase;
  }

  .contact-list {
    position: absolute; left: 34px; top: 104px;
    list-style: none;
    font-size: 10.5px; line-height: 15px; color: var(--ink);
    letter-spacing: 0.6px;
  }
  .contact-list li { display: flex; align-items: center; gap: 8px; }
  .contact-list li::before {
    content: ""; width: 6px; height: 6px; border-radius: 50%;
    background: var(--green-mid); flex: none;
  }
  .contact-list li.cont::before { background: transparent; }

  .front-band { position: absolute; left: 0; bottom: 0; width: 520px; height: 110px; }
  .holder-name {
    position: absolute; right: 40px; top: 196px;
    font-size: 13px; letter-spacing: 3px; color: var(--green-mid);
    text-transform: uppercase; font-weight: 600;
  }
  .front-web {
    position: absolute; right: 40px; bottom: 16px;
    font-size: 9px; letter-spacing: 3px; color: #ffffff;
  }

  .back-web {
    position: absolute; left: 40px; top: 36px;
    font-size: 14px; letter-spacing: 6px; color: #e5efe0;
    text-transform: uppercase; font-weight: 600;
  }
  .back-mark {
    position: absolute; right: 34px; top: 128px;
    font-size: 64px; font-weight: 700; letter-spacing: 4px;
    color: rgba(255,255,255,0.10); text-transform: uppercase;
  }
</style>
</head>
<body>
  <section class="card card-front">
    <div class="brand">
      <span class="brand-mark"></span>
      <span class="brand-name">Twin-Kay</span>
    </div>
    <div class="brand-tagline">Research &amp; Manufacturing</div>

    <ul class="contact-list">
      <li>Rustomji Parekh Building,</li>
      <li class="cont">58 Hill Street, Fortm</li>
      <li class="cont">Mumbai 400019 India</li>
      <li>+91 22 4017 5530</li>
      <li>+91 98200 41716</li>
      <li>vikram@twin-kay.com</li>
      <li>www.twin-kay.com</li>
    </ul>

    <svg class="front-band" viewBox="0 0 520 110" aria-hidden="true">
      <defs>
        <linearGradient id="bandFill" x1="0" y1="0" x2="1" y2="0">
          <stop offset="0" stop-color="#5a8a4c"/>
          <stop offset="1" stop-color="#3f6b35"/>
        </linearGradient>
      </defs>
      <path d="M0 40 L150 40 Q175 40 190 62 Q205 84 235 84 L520 84 L520 110 L0 110 Z" fill="url(#bandFill)"/>
      <path d="M0 34 L150 34 Q178 34 194 58" fill="none" stroke="#cfe0c6" stroke-width="2"/>
    </svg>
    <div class="holder-name">Vikram Talwarkar</div>
    <div class="front-web">www.twin-kay.com</div>
  </section>

  <section class="card card-back">
    <div class="back-web">www.twin-kay.com</div>
    <div class="back-mark">Twin-Kay</div>
  </section>
</body>
</html>
```